Brisk Tissu, wipes multipack branding 3 types in 1 family

Brisk Tissu is a wipe producing company. For some information see our (not completed) website at briskissu.nl. We also have a product named Palmora (see Palmora.com).
Our philosophy is to produce environmental friendly wipes only. We are doing that by using both bamboo and 100% bioviscose as Nonwoven. Both are biodegradable and compostable. We produce single packed wipes and multipacks (think about hygiene for hand, deodorant wipes and playtime wipes (for cleaning sex toys)). We are looking for designs for our multipacks (6 to 10 pieces per package). The size of the unfolded package foil is about 150 x 190mm (width x height) (but varies depending on the material and the number of wipes).
The branding should be modern, fresh and in line with our thoughts.

We want to have 3 packages designed for:
- Purely2Palms multipack 6 pieces
- Deodorant wipes multipack 6 pieces
- Playtime wipes multipack 10 pieces
All should have the look and feel of our Brisk Tissu logo / branding, and belong to the same family of products (to be recognised they belong together).

I added our logo as well as some examples of other packages we have been creating as samples. At first we have been thinking about using that design for multipacks as well, but we were not that happy about that.
Please consider them as a style that we liked.

Target Market(s)

Consumers
- Festival people (Purely2Palms and Deodorant)
- Adults with children (Purely2Palms)
- Travelers (Purely2Palm and Deodorant)
- Business people (Deodorant)
- Erotic industry (Playtime wipes)

Font styles to use
Sans Serif

Colors

Designer to choose colors to be used in the design.

Requirements
Must have
• A family in branding, recognisability as being part of 1 family of products.
• Branded with our logo (as attached).
• Necessary and mandatory information on the back of the package.
Nice to have
• Designs that fit to the purpose of the wipes.
• Different Colors for the different products.
• Chosen font is just because it is modern. Could be any other modern font as well.
Should not have
• Old fashioned style.
• Too much focus on the "green-ness" of the products.

```html
<!DOCTYPE html>
<html lang="en">
<head>
<meta charset="utf-8">
<title>Brisk Tissu – multipack family</title>
<link rel="stylesheet" href="https://fonts.googleapis.com/css2?family=Josefin+Sans:wght@300;400;600;700&family=Open+Sans:wght@400;600&display=swap">
<style>
  :root{
    --stage:#d6d6d8;
    --foil:#f2f2f3;
    --deo:#b8334f;
    --deo-accent:#eab9c2;
    --hands:#294b70;
    --hands-accent:#8ecdd0;
    --play:#6e2c5e;
    --play-accent:#e8b3be;
    --ink-light:#ffffff;
  }
  *{box-sizing:border-box;margin:0;padding:0}
  html,body{width:857px;height:1200px;overflow:hidden}
  body{background:var(--stage);position:relative;font-family:"Josefin Sans",sans-serif}

  .pack{position:absolute;left:88px;width:696px;height:320px;display:flex;overflow:hidden}
  .pack--deo{top:64px;--brand:var(--deo);--accent:var(--deo-accent)}
  .pack--hands{top:446px;--brand:var(--hands);--accent:var(--hands-accent)}
  .pack--play{top:820px;--brand:var(--play);--accent:var(--play-accent)}

  .pack__front{position:relative;width:357px;height:100%;background:var(--foil)}
  .pack__product{position:relative;flex:1;height:100%;background:var(--brand);color:var(--ink-light)}

  .splash{position:absolute;left:0;top:92px;width:184px;height:228px;
    background:radial-gradient(ellipse at 60% 70%,var(--brand) 0%,var(--brand) 45%,rgba(255,255,255,0) 75%)}

  .brand{position:absolute;left:140px;top:30px;display:flex;align-items:center;gap:12px;color:var(--brand)}
  .brand__mark{width:44px;height:44px;background:var(--brand)}
  .brand__name{font-weight:600;font-size:36px;line-height:32px;letter-spacing:1px;text-transform:uppercase}

  .origin{position:absolute;right:40px;top:116px;text-align:right;color:var(--brand);font-weight:300;font-size:14px;line-height:18px}
  .site{position:absolute;right:40px;top:172px;color:var(--brand);font-weight:300;font-size:13.5px}

  .feature{position:absolute;top:250px;width:80px;margin-left:-40px;text-align:center;
    font-family:"Open Sans",sans-serif;font-size:7.5px;line-height:9.5px;font-weight:600}
  .feature svg{display:block;margin:0 auto 4px;width:24px;height:24px}
  .pack__front .feature{color:#222}
  .pack__product .feature{color:rgba(255,255,255,.85);font-weight:400}

  .product-art{position:absolute;left:140px;top:50px;width:60px;height:58px;border-radius:50%;
    background:rgba(255,255,255,.18)}
  .title{position:absolute;left:0;right:0;top:118px;text-align:center;font-weight:700;font-size:46px;line-height:48px;letter-spacing:2px;text-transform:uppercase}
  .title__top{color:var(--ink-light)}
  .title__bottom{color:var(--accent)}
  .claims{position:absolute;left:180px;top:250px;font-weight:400;font-size:11.5px;line-height:15px;letter-spacing:.2px;text-transform:uppercase}
</style>
</head>
<body>

<!-- Deodorant -->
<section class="pack pack--deo">
  <div class="pack__front">
    <div class="splash" role="img" aria-label="Liquid splash illustration in red"></div>
    <div class="brand"><span class="brand__mark"></span><span class="brand__name">Brisk<br>Tissu</span></div>
    <p class="origin">Made in the EU,<br>Designed by Brisk Tissu</p>
    <p class="site">www.briskissu.nl</p>
    <div class="feature" style="left:220px"><svg viewBox="0 0 24 24" role="img" aria-label="Cleansing icon"><circle cx="12" cy="12" r="8" fill="none" stroke="currentColor" stroke-width="1.5"/></svg>Deep<br>Cleansing</div>
    <div class="feature" style="left:306px"><svg viewBox="0 0 24 24" role="img" aria-label="Healthy skin icon"><circle cx="12" cy="12" r="8" fill="none" stroke="currentColor" stroke-width="1.5"/></svg>Promotes<br>Healthy Skin</div>
  </div>
  <div class="pack__product">
    <div class="product-art" role="img" aria-label="Line illustration of an underarm"></div>
    <h2 class="title"><span class="title__top">Deo</span><br><span class="title__bottom">Wipe</span></h2>
    <div class="feature" style="left:49px"><svg viewBox="0 0 24 24" role="img" aria-label="Antibacterial icon"><circle cx="12" cy="12" r="6" fill="currentColor"/></svg>Anti-bacterial<br>Wipes</div>
    <div class="feature" style="left:137px"><svg viewBox="0 0 24 24" role="img" aria-label="Impurities icon"><path d="M3 18h18" stroke="currentColor" stroke-width="1.5"/><circle cx="9" cy="14" r="2" fill="currentColor"/><circle cx="14" cy="14" r="2" fill="currentColor"/></svg>Gently Remove<br>Impurities</div>
    <p class="claims">With antibacterial<br>effectiveness<br>biodegradable</p>
  </div>
</section>

<!-- Hands -->
<section class="pack pack--hands">
  <div class="pack__front">
    <div class="splash" role="img" aria-label="Liquid splash illustration in blue"></div>
    <div class="brand"><span class="brand__mark"></span><span class="brand__name">Brisk<br>Tissu</span></div>
    <p class="origin">Made in the EU,<br>Designed by Brisk Tissu</p>
    <p class="site">www.briskissu.nl</p>
    <div class="feature" style="left:220px"><svg viewBox="0 0 24 24" role="img" aria-label="Cleansing icon"><circle cx="12" cy="12" r="8" fill="none" stroke="currentColor" stroke-width="1.5"/></svg>Deep<br>Cleansing</div>
    <div class="feature" style="left:306px"><svg viewBox="0 0 24 24" role="img" aria-label="Healthy skin icon"><circle cx="12" cy="12" r="8" fill="none" stroke="currentColor" stroke-width="1.5"/></svg>Promotes<br>Healthy Skin</div>
  </div>
  <div class="pack__product">
    <div class="product-art" role="img" aria-label="Line illustration of a hand holding a wipe"></div>
    <h2 class="title"><span class="title__top">Purely</span><br><span class="title__bottom">2Palms</span></h2>
    <div class="feature" style="left:49px"><svg viewBox="0 0 24 24" role="img" aria-label="Antibacterial icon"><circle cx="12" cy="12" r="6" fill="currentColor"/></svg>Anti-bacterial<br>Wipes</div>
    <div class="feature" style="left:137px"><svg viewBox="0 0 24 24" role="img" aria-label="Impurities icon"><path d="M3 18h18" stroke="currentColor" stroke-width="1.5"/><circle cx="9" cy="14" r="2" fill="currentColor"/><circle cx="14" cy="14" r="2" fill="currentColor"/></svg>Gently Remove<br>Impurities</div>
    <p class="claims">With antibacterial<br>effectiveness<br>biodegradable</p>
  </div>
</section>

<!-- Intimate care -->
<section class="pack pack--play">
  <div class="pack__front">
    <div class="splash" role="img" aria-label="Liquid splash illustration in plum"></div>
    <div class="brand"><span class="brand__mark"></span><span class="brand__name">Brisk<br>Tissu</span></div>
    <p class="origin">Made in the EU,<br>Designed by Brisk Tissu</p>
    <p class="site">www.briskissu.nl</p>
    <div class="feature" style="left:220px"><svg viewBox="0 0 24 24" role="img" aria-label="Cleansing icon"><circle cx="12" cy="12" r="8" fill="none" stroke="currentColor" stroke-width="1.5"/></svg>Deep<br>Cleansing</div>
    <div class="feature" style="left:306px"><svg viewBox="0 0 24 24" role="img" aria-label="Healthy skin icon"><circle cx="12" cy="12" r="8" fill="none" stroke="currentColor" stroke-width="1.5"/></svg>Promotes<br>Healthy Skin</div>
  </div>
  <div class="pack__product">
    <div class="product-art" role="img" aria-label="Line illustration of a couple with hearts"></div>
    <h2 class="title"><span class="title__top">Tenderly</span><br><span class="title__bottom">Wipe</span></h2>
    <div class="feature" style="left:49px"><svg viewBox="0 0 24 24" role="img" aria-label="Antibacterial icon"><circle cx="12" cy="12" r="6" fill="currentColor"/></svg>Anti-bacterial<br>Wipes</div>
    <div class="feature" style="left:137px"><svg viewBox="0 0 24 24" role="img" aria-label="Impurities icon"><path d="M3 18h18" stroke="currentColor" stroke-width="1.5"/><circle cx="9" cy="14" r="2" fill="currentColor"/><circle cx="14" cy="14" r="2" fill="currentColor"/></svg>Gently Remove<br>Impurities</div>
    <p class="claims">With antibacterial<br>effectiveness<br>biodegradable</p>
  </div>
</section>

</body>
</html>
```